Pillar Orchard
Professional
Mira Castellan, MBA
mira@pillarorchard.ca
www.pillarorchard.ca
Landscape layout. Please include tagline: "Building Momentum for Success"
Whatever you think will look good.

```html
<!DOCTYPE html>
<html lang="en">
<head>
<meta charset="utf-8">
<title>Pillar Orchard – Business Card</title>
<link rel="stylesheet" href="https://fonts.googleapis.com/css2?family=Open+Sans:wght@400;600;700&display=swap">
<style>
  :root {
    --stage: #2b2b2d;
    --card: #ffffff;
    --brand-blue: #1e4596;
    --brand-blue-deep: #12306e;
    --ink: #1a1a1a;
    --muted: #55585f;
    --charcoal: #2c2c2e;
    --silver: #b9bcc2;
  }
  * { margin: 0; padding: 0; box-sizing: border-box; }
  html, body {
    width: 1200px; height: 906px; overflow: hidden;
    background: var(--stage);
    font-family: "Open Sans", Arial, sans-serif;
  }
  .business-card {
    position: absolute;
    left: 160px; top: 173px;
    width: 880px; height: 560px;
    background: var(--card);
    border-radius: 34px;
    overflow: hidden;
    box-shadow: 0 18px 40px rgba(0,0,0,0.45);
  }
  .card-swooshes { position: absolute; inset: 0; width: 100%; height: 100%; }
  .brand-lockup {
    position: absolute; left: 42px; top: 118px;
    display: flex; align-items: center; gap: 20px;
  }
  .brand-dot {
    width: 96px; height: 96px; border-radius: 50%;
    background: var(--brand-blue-deep);
  }
  .brand-name {
    color: var(--brand-blue);
    font-weight: 700;
    font-size: 46px;
    line-height: 0.98;
    letter-spacing: 2px;
    text-transform: uppercase;
  }
  .tagline {
    position: absolute; left: 158px; top: 226px;
    color: var(--muted);
    font-weight: 600; font-size: 17px;
    letter-spacing: 0.5px;
  }
  .holder-name {
    position: absolute; left: 430px; top: 262px;
    color: var(--brand-blue);
    font-weight: 700; font-size: 31px;
    white-space: nowrap;
  }
  .contact-list {
    position: absolute; right: 60px; top: 370px;
    list-style: none; text-align: right;
    color: var(--ink); font-size: 21px; line-height: 36px;
  }
  .contact-label { color: var(--brand-blue); font-weight: 600; }
</style>
</head>
<body>
  <main class="business-card">
    <svg class="card-swooshes" viewBox="0 0 880 560" aria-hidden="true">
      <defs>
        <linearGradient id="blueSweep" x1="0" y1="0" x2="1" y2="1">
          <stop offset="0" stop-color="#3461c1"/>
          <stop offset="1" stop-color="#112a66"/>
        </linearGradient>
      </defs>
      <path d="M300 0 H880 V250 C820 140 640 70 300 0 Z" fill="var(--charcoal)"/>
      <path d="M340 0 H880 V215 C810 110 640 45 340 0 Z" fill="url(#blueSweep)"/>
      <path d="M300 0 C640 70 820 140 880 250 V262 C815 150 640 80 290 0 Z" fill="var(--silver)"/>
      <path d="M0 400 C90 470 190 530 300 560 H0 Z" fill="var(--charcoal)"/>
      <path d="M0 440 C70 495 160 538 250 560 H0 Z" fill="url(#blueSweep)"/>
    </svg>

    <div class="brand-lockup">
      <span class="brand-dot"></span>
      <div class="brand-name">Pillar<br>Orchard</div>
    </div>
    <p class="tagline">Building Momentum for Success</p>

    <h1 class="holder-name">Mira Castellan, MBA</h1>

    <ul class="contact-list">
      <li><span class="contact-label">P :</span> 604-555-0182</li>
      <li><span class="contact-label">E :</span> mira@pillarorchard.ca</li>
      <li>www.pillarorchard.ca</li>
    </ul>
  </main>
</body>
</html>
```